Corporate services company needs a brochure

We are starting a company offering setup services to companies new to that location.
This includes services such as recruitment, company formation, advertising, marketing, pr, handling legal issues, logistics, transportation, procurement,immigration services, corporate gifts, accomodation,entertainment, training, administrative services etc.
Basically taking the setup issues off the hands of the company allowing them focus on their core business.

We are looking to design a professional brochure which would give the potential customers the confidence to entrust us with their needs.

We will be including some copy that can be used but i would very much like for you to bring what i have written to life - adding, deducting and amending where required.

We are looking at a A4 4/6 paged brochure but open to suggestions.

                                       

If you have any images that are suitable, please let us know. We will also be searching for some to add.

The first prize has been increased.

Thanks

Reason: We have just guaranteed the payment and we are hoping that this will encourage good designers to participate.

Reason: Some designers have requested more time to complete their final design.

Hi, I h extended the deadline to give designers more time to work on designs.

we are also looking at making the brochure a height of 8.5 and a width of 11. Please let me know your thoughts on this as any advice will help. The whole objective is to make it look as up to date and creative as possible. There is also another design size of 7.5 by 8.5

Thanks

                                        Hi

The copy has been revised and uploaded.

Hopefully it will give a clearer explanation of what we are trying to do.

Please let me know if you have any further questions.

Thanks

Marta

Reason: adding finishing touches to designs

Reason: We are amending the copy for the brochure

Reason: The new copy for the brochure is ready. I am sorry it has taken so long to get it out. I am sure we will not be making any amendments to it post today. Thanks for your patience The extension is not to attact new designs it is for existing designs's copy to be modified to include information from the updated copy.

Target Market(s)

medium to large companies in banking, telecom, retail etc. It will be viewed by middle and top management.

Industry/Entity Type

Legal

Requirements
Must have
• The brochure must clearly highlight all our services without just listing as this would risk it appearing as if we have just included everything we could think of!,
Please do not do the sitting round the conference table brochure or the typical blue and white brochure.
I desperately need it to be different, unique and serious enough to show that we are capable of handling/managing all what we have included.
Our clients include the many companies starting up an office in Africa.
We are anxious to have the potential clients understand that we will help them setup under any climax/
Nice to have
• modern colours but not too bright. there must still be a clear serious edge to it.
Should not have
• conference room table and people sitting around it.
the typical blue and white brochures often used for these type of services.

```html
<!DOCTYPE html>
<html lang="en">
<head>
<meta charset="utf-8">
<title>More About Us – Orvela</title>
<link rel="stylesheet" href="https://fonts.googleapis.com/css2?family=Delius&family=Nunito+Sans:wght@400;800;900&family=Roboto+Condensed:ital,wght@1,700&display=swap">
<style>
  :root {
    --purple: #5b3a98;
    --teal: #137d6d;
    --lime: #8cc63f;
    --sky: #9cc0e8;
    --body-green: #4f8a34;
    --panel: #eef3dc;
    --white: #ffffff;
  }
  * { margin: 0; padding: 0; box-sizing: border-box; }
  html, body { width: 1200px; height: 1200px; overflow: hidden; }
  body { position: relative; background: var(--white); font-family: "Nunito Sans", Arial, sans-serif; }

  .frame-pattern {
    position: absolute; inset: 0;
    background: linear-gradient(135deg, var(--purple) 0%, var(--teal) 30%, var(--lime) 55%, var(--sky) 78%, var(--purple) 100%);
  }
  .panel {
    position: absolute; left: 115px; top: 107px; width: 973px; height: 983px;
    background: var(--panel);
    outline: 4px solid var(--white);
  }

  .page-title {
    position: absolute; left: 155px; top: 128px;
    font-family: "Delius", cursive; font-weight: 400;
    font-size: 74px; color: var(--teal); letter-spacing: -0.5px; line-height: 1.1;
  }
  .section-title {
    position: absolute;
    font-family: "Delius", cursive; font-weight: 400;
    font-size: 45px; color: var(--teal); line-height: 1.1;
  }

  .col-left { position: absolute; left: 165px; width: 436px; }
  .col-right { position: absolute; left: 670px; width: 349px; }

  .mission-quote {
    top: 218px;
    font-weight: 900; font-size: 23px; line-height: 26px;
    color: var(--purple); text-align: justify; text-align-last: left;
  }
  .copy {
    font-size: 19.5px; line-height: 26px; color: var(--body-green);
    text-align: justify;
  }
  .copy p { text-align: justify; }
  .intro { top: 316px; }

  .values {
    position: absolute; left: 165px; top: 670px; list-style: none;
    font-family: "Roboto Condensed", Arial, sans-serif; font-style: italic; font-weight: 700;
    font-size: 20px; line-height: 29px; color: var(--purple);
  }
  .values li::before { content: "•"; font-style: normal; font-size: 14px; margin-right: 10px; position: relative; top: -2px; }

  .message { top: 773px; }
  .brains-title { left: 162px; top: 856px; }
  .brains-copy { top: 925px; }

  .advice-copy { top: 224px; line-height: 33px; }
  .brawn-title { left: 668px; top: 458px; }
  .brawn-copy { top: 511px; line-height: 33px; }

  .dancers-art {
    position: absolute; left: 715px; top: 845px; width: 285px; height: 230px;
    background: radial-gradient(ellipse at center, rgba(91,58,152,0.35) 0%, rgba(19,125,109,0.18) 55%, rgba(238,243,220,0) 75%);
  }
</style>
</head>
<body>
  <div class="frame-pattern" role="img" aria-label="Decorative border of geometric African-style painted patterns in purple, teal, lime green and light blue"></div>

  <main class="panel"></main>

  <h1 class="page-title">More About Us</h1>

  <p class="col-left mission-quote">“We are committed to providing excellence and inspiring confidence in everything we do.</p>

  <div class="col-left copy intro">
    <p>We are a dynamic and growing business, focused on meeting the changing needs of our clients.</p>
    <p>Our people are the secret to our success. By harnessing their expertise, we are consistently delivering value for our clients on projects around the world”.</p>
    <p>Our focus at Orvela is simple: It is to be the best in class consultant in all that we do.</p>
    <p>This success inspires confidence from our clients and pride from our people.</p>
    <p>We do it by respecting 3 fundamental values:</p>
  </div>

  <ul class="values">
    <li>Being imaginative in everything we do</li>
    <li>Being purposeful in everything we do</li>
    <li>Being dependable in everything we do</li>
  </ul>

  <p class="col-left copy message">That is why our message for clients, staff and partners is clear – ‘ORVELA, creative minds, and safe hands’.</p>

  <h2 class="section-title brains-title">Brains!</h2>
  <p class="col-left copy brains-copy">Through a series of consultations, we help you determine how to transform your business. In the early stages of your company, having access to experienced business people is essential.</p>

  <p class="col-right copy advice-copy">Getting the right advice can be the difference between failure and success. We will help you find the people whose background fits our particular situation and leverage their knowledge to accelerate your growth.</p>

  <h2 class="section-title brawn-title">Brawn!</h2>
  <p class="col-right copy brawn-copy">There is no substitute for experience, especially in early stage companies that typically do not have the financial resources to hire full time executives. We will help you determine those areas – business plan, marketing, legal, procurement, finance – that need immediate attention and provide</p>

  <div class="dancers-art" role="img" aria-label="Illustration of three dancing women in colourful patterned dresses and head wraps"></div>
</body>
</html>
```